Business Cards for new orthopaedic surgery practice

My husband and I are starting our own orthopaedic surgery practice. We are looking for a business card that is uniform, but one will have my name/title and the other will have his. You can just create one design with my name on it for now. But when I choose your design as the winning design I will ask that you add another copy with his name/title.

We are looking for classy, simple, elite all in one. We like dark blues/a little gold/yellow. Something that goes with our logo. We want our logo incorporated. Here is all the info you need:
Business name: RV Spine & Vitality Center
Location: 38915 North Bramble Ave
Palm Hollow, FL 33490
Phone: 954-218-4630
Fax: 954-571-2846
Email: info@myrvspine.example

Names: Lucinda Ferrow, M.D.
Board Certified Hand and Upper Extremity Surgeon

Emeka Dlunga, M.D.
Board Certified Hip & Knee Replacement/General Orthopaedic Surgeon

Can decide what you want to put on the back. Maybe a slogan:
Grounded in Care. Centered on You

I am just going to upload our logo. The only thing is if we select you as the winning design, the location, and phone numbers may change. We will need your help to update that once fully solidified.

Industry/Entity Type

Medical

Contact Information for Business Card

Colors
0054AA
0677BA
7BADD7
CADEEF
E8F1F8
0094D4
00A9DD
6FCCEA
C7EBF8
E9F6FB

Requirements
Must have
• class, appeal,
Should not have
• We want to air on the side of masculine if we are looking at masculine vs. feminine feel. But we still want it classy, sophisticated, and something we will love

```html
<!DOCTYPE html>
<html lang="en">
<head>
<meta charset="utf-8">
<title>RV Spine &amp; Vitality Center — Business Card</title>
<link rel="stylesheet" href="https://fonts.googleapis.com/css2?family=Cinzel:wght@500&family=Poppins:wght@400;500&family=Roboto:wght@900&display=swap">
<style>
  :root {
    --navy: #1c2a4f;
    --gold: #c6a15b;
    --white: #ffffff;
    --backdrop: #c9c9c9;
  }
  * { box-sizing: border-box; margin: 0; padding: 0; }
  html, body { width: 1200px; height: 1015px; overflow: hidden; }
  body {
    background: var(--backdrop);
    font-family: "Poppins", sans-serif;
    position: relative;
  }
  .card {
    position: absolute;
    left: 290px;
    width: 620px;
    height: 354px;
    background: var(--navy);
    overflow: hidden;
    box-shadow: 0 6px 18px rgba(0,0,0,0.25);
  }
  /* Logo side */
  .card--brand { top: 110px; }
  .brand-lockup {
    position: absolute;
    left: 0; right: 0; top: 70px;
    display: flex; flex-direction: column; align-items: center; gap: 18px;
  }
  .brand-mark {
    width: 44px; height: 44px; border-radius: 50%;
    border: 2px solid var(--gold);
  }
  .brand-name {
    font-family: "Poppins", sans-serif;
    font-weight: 500;
    font-size: 24px;
    letter-spacing: 0.06em;
    color: var(--white);
  }
  .slogan {
    position: absolute;
    left: 0; right: 0; top: 250px;
    text-align: center;
    font-family: "Roboto", sans-serif;
    font-weight: 900;
    font-size: 21px;
    color: var(--white);
  }
  .slogan__accent { color: var(--gold); }

  /* Contact side */
  .card--contact { top: 551px; }
  .emblem-area {
    position: absolute;
    right: 0; top: 0;
    width: 180px; height: 100%;
    background: var(--gold);
  }
  .emblem-area__light {
    position: absolute;
    right: 70px; top: 0;
    width: 150px; height: 326px;
    background: var(--white);
    border-bottom-right-radius: 18px;
  }
  .navy-field {
    position: absolute;
    left: 0; top: 0;
    width: 520px; height: 326px;
    background: var(--navy);
    border-bottom-right-radius: 18px;
  }
  .gold-strip {
    position: absolute; left: 0; bottom: 0;
    width: 100%; height: 8px; background: var(--gold);
  }
  .person {
    position: absolute; left: 42px; top: 52px;
  }
  .person__name {
    font-family: "Cinzel", serif;
    font-weight: 500;
    font-size: 28px;
    color: var(--gold);
    letter-spacing: 0.02em;
  }
  .person__title {
    margin-top: 8px;
    font-size: 15px;
    line-height: 1.25;
    color: var(--white);
  }
  .contact-list {
    position: absolute; left: 42px; top: 190px;
    list-style: none;
    color: var(--white);
    font-size: 15px;
    line-height: 1.2;
  }
  .contact-list li { display: flex; align-items: center; gap: 10px; margin-bottom: 6px; }
  .contact-list li.address { margin-bottom: 14px; }
  .icon {
    flex: none;
    width: 22px; height: 22px; border-radius: 50%;
    background: var(--gold);
    display: flex; align-items: center; justify-content: center;
  }
  .icon svg { width: 12px; height: 12px; fill: var(--white); }
</style>
</head>
<body>

<section class="card card--brand">
  <div class="brand-lockup">
    <span class="brand-mark" aria-hidden="true"></span>
    <span class="brand-name">RV Spine &amp; Vitality Center</span>
  </div>
  <p class="slogan">Grounded in Care. <span class="slogan__accent">Centered on You</span></p>
</section>

<section class="card card--contact">
  <div class="emblem-area" role="img" aria-label="Large decorative practice emblem in white and gold">
    <div class="emblem-area__light"></div>
  </div>
  <div class="navy-field"></div>
  <div class="gold-strip"></div>

  <div class="person">
    <h1 class="person__name">Lucinda Ferrow, M.D.</h1>
    <p class="person__title">Board Certified Hand and Upper<br>Extremity Surgeon</p>
  </div>

  <ul class="contact-list">
    <li class="address">
      <span class="icon"><svg viewBox="0 0 12 12"><path d="M6 0a4 4 0 0 0-4 4c0 3 4 8 4 8s4-5 4-8a4 4 0 0 0-4-4zm0 5.5A1.5 1.5 0 1 1 6 2.5a1.5 1.5 0 0 1 0 3z"/></svg></span>
      <span>38915 North Bramble Ave<br>Palm Hollow, FL 33490</span>
    </li>
    <li>
      <span class="icon"><svg viewBox="0 0 12 12"><path d="M2.5 0.5l2 2-1 1.5c.8 1.6 2 2.8 3.5 3.5l1.5-1 2 2-1.5 2C5 10 2 7 .5 2z"/></svg></span>
      <span>954-218-4630</span>
    </li>
    <li>
      <span class="icon"><svg viewBox="0 0 12 12"><rect x="3" y="0.5" width="6" height="3"/><rect x="0.5" y="4" width="11" height="5" rx="1"/><rect x="3" y="8" width="6" height="3.5"/></svg></span>
      <span>954-571-2846</span>
    </li>
    <li>
      <span class="icon"><svg viewBox="0 0 12 12"><path d="M0.5 2.5h11v7h-11z M0.5 2.5l5.5 4 5.5-4" fill="none" stroke="#fff" stroke-width="1.2"/></svg></span>
      <span>info@myrvspine.example</span>
    </li>
  </ul>
</section>

</body>
</html>
```